Online Marketplace Startup for Community Facilities (Tovaroom)

A innovative, modern website design is required for a new startup called Tovaroom. Tovaroom will be an online marketplace for searching for and booking community facilities, such as schools facilities (sports grounds, halls, classrooms etc.), churches, hospitals and other community facilities.

The attached brief has been created to provide guidance on the structure and content required.

The web design shall feature a modern, innovative but user friendly interface similar style to other web start up pages:
www.hallquiver.co.uk
www.vendlark.com.au
www.artfennel.com.au

The web design shall be ‘wordpress’ compliant and allow for future functionality to be added and coded (e.g. animations, flash, blogs etc) and content to be editable.

The following brief has been created to provide guidance on the structure and content required.

An existing logo developed for Tovaroom shall be utilised and incorporated in the top left hand cover of the cover landing page (refer to attached logo designs).

Refer to attached 'Website brief' for more details on requirements.
Updates

Project Deadline Extended
Reason: I wish to grant an extension to the deadline to provide designers with more time to submit their designs.

Target Market(s)

TovaRoom will focus on building a customer network of both community facility owners (schools, hospitals, churches) and hirers (non-government organisations, community groups, event management companies, commercial businesses). Members of the general public will also be encouraged to book facilities for private functions.

Industry/Entity Type

Community

Coding

Coded - Design and coding required

Number of Pages Required

5+ page

Font styles to use
Sans Serif

Colors
3176b5
ffffff
85cae6
33a6d7

Requirements
Must have
• The web design shall feature a modern, innovative but user friendly interface similar style to other web start up pages:
• www.hallquiver.co.uk
• www.vendlark.com.au
• www.artfennel.com.au
• The web design shall be ‘wordpress’ compliant and allow for future functionality to be added and coded (e.g. animations, flash, blogs etc) and content to be editable.
• Refer to Project brief for other requirements
Nice to have
• Refer to Project brief
Should not have
• Refer to Project brief

```html
<!DOCTYPE html>
<html lang="en">
<head>
<meta charset="utf-8">
<title>Tovaroom – Community Facility Bookings</title>
<link rel="stylesheet" href="https://fonts.googleapis.com/css2?family=Montserrat:wght@300;400;500;600;700&family=Open+Sans:wght@300;400;600&display=swap">
<style>
:root{
  --blue:#2c60b1;
  --blue-mid:#4b76b8;
  --blue-dark:#1f3f78;
  --navy:#1b2f55;
  --band:rgba(44,96,177,.85);
  --red:#e0453b;
  --red-dark:#a71b14;
  --step-blue:#4c78bb;
  --step-blue-dark:#3b1f22;
  --green:#3f911b;
  --green-dark:#16300a;
  --yellow:#f8bd0c;
  --yellow-dark:#2f5c14;
  --gold:#f9c04b;
  --ink:#222;
  --muted:#555;
  --white:#fff;
  --line:#d8d8d8;
}
*{margin:0;padding:0;box-sizing:border-box}
html,body{width:1200px;height:2601px;overflow:hidden}
body{position:relative;font-family:'Montserrat',sans-serif;color:var(--ink);background:var(--white)}
.abs{position:absolute}

/* hero */
.hero{left:0;top:0;width:1200px;height:550px;overflow:hidden}
.hero-photo{position:absolute;inset:0;background:
  radial-gradient(ellipse at 70% 40%,#8a6a5a 0%,transparent 55%),
  radial-gradient(ellipse at 25% 70%,#4b5360 0%,transparent 60%),
  linear-gradient(110deg,#6f6a66 0%,#4a4b52 40%,#3b3f4a 70%,#2a3040 100%)}
.hero-shade{position:absolute;inset:0;background:rgba(20,24,34,.35)}
.brand{display:flex;align-items:center;gap:10px;color:var(--white);font-weight:400}
.brand-mark{width:30px;height:30px;border-radius:50%;background:var(--white)}
.header-brand{left:152px;top:38px;font-size:28px}
.nav{left:430px;top:47px;display:flex;gap:27px;font-size:11.5px;font-weight:500;color:var(--white);letter-spacing:.3px}
.nav .active{font-weight:700}
.nav-cta{left:940px;top:39px;width:109px;height:32px;background:var(--blue);color:var(--white);font-size:10.5px;font-weight:700;display:flex;align-items:center;justify-content:center}
.hero-title{left:0;top:180px;width:1200px;text-align:center;color:var(--white);font-size:31px;font-weight:300;line-height:37px}
.hero-title b{font-weight:700}
.hero-btn{left:518px;top:322px;width:162px;height:37px;border:2px solid var(--white);color:var(--gold);font-size:14px;font-weight:700;letter-spacing:1px;display:flex;align-items:center;justify-content:center}
.hero-band{left:0;top:472px;width:1200px;height:78px;background:var(--band);color:var(--white);font-family:'Open Sans',sans-serif;font-weight:300;font-size:22px;display:flex;align-items:center;padding-left:183px}

/* process */
.eyebrow{width:1200px;left:0;text-align:center;font-weight:500;letter-spacing:1px}
.process-eyebrow{top:627px;font-size:14px;color:var(--ink)}
.section-title{width:1200px;left:0;text-align:center;font-weight:700;color:var(--blue);letter-spacing:1px}
.process-title{top:647px;font-size:29px}
.process-sub{left:0;top:690px;width:1200px;text-align:center;font-family:'Open Sans',sans-serif;font-size:12px;color:var(--muted)}
.step{width:260px;height:260px;margin:-130px 0 0 -130px}
.step-shape{position:absolute;left:38px;top:38px;width:184px;height:184px;border-radius:30px;transform:rotate(45deg)}
.step-icon{position:absolute;left:100px;top:40px;width:60px;height:60px}
.step-text{position:absolute;left:72px;top:116px;width:116px;text-align:center;color:var(--white);font-family:'Open Sans',sans-serif;font-size:10.5px;line-height:13px}
.step-num{position:absolute;left:0;top:108px;width:44px;height:44px;border-radius:50%;border:3px solid var(--white);color:var(--white);font-size:19px;font-weight:700;display:flex;align-items:center;justify-content:center}
.step-1 .step-shape{background:var(--red)} .step-1 .step-num{background:var(--red-dark)}
.step-2 .step-shape{background:var(--step-blue)} .step-2 .step-num{background:var(--step-blue-dark)}
.step-3 .step-shape{background:var(--green)} .step-3 .step-num{background:var(--green-dark)}
.step-4 .step-shape{background:var(--yellow)} .step-4 .step-num{background:var(--yellow-dark)}
.step-1 .step-num{left:4px}

/* services */
.services{left:0;top:1087px;width:1200px;height:618px;background:linear-gradient(#ececec 0,#fafafa 40px,#fbfbfb 100%)}
.services-title{top:1160px;font-size:29px;color:var(--navy)}
.services-eyebrow{top:1201px;font-size:10px;font-weight:700;color:var(--ink)}
.card{background:var(--white);border:1px solid #e6e6e6;text-align:center}
.card-art{position:absolute;left:50%;width:96px;height:92px;margin-left:-48px;border-radius:6px}
.card-name{position:absolute;left:0;width:100%;font-size:13px;line-height:17px;font-weight:500;color:var(--ink)}
.card-btn{position:absolute;left:50%;width:104px;height:23px;margin-left:-52px;background:var(--blue-mid);color:var(--white);font-family:'Open Sans',sans-serif;font-size:9.5px;display:flex;align-items:center;justify-content:center}
.card.featured{box-shadow:0 8px 22px rgba(0,0,0,.18);border:none}
.card.featured .card-btn{background:var(--gold);box-shadow:0 3px 0 #f3e0b3}
.card-copy{position:absolute;left:20px;width:196px;font-family:'Open Sans',sans-serif;font-size:9.5px;line-height:13px;color:var(--muted)}
.dots{left:575px;top:1627px;display:flex;gap:6px}
.dots i{width:12px;height:12px;background:#d6d6d6}
.dots i:first-child{background:var(--blue-mid)}

/* clients */
.clients{left:0;top:1705px;width:1200px;height:277px;background:linear-gradient(90deg,#1d3766 0%,#25467f 55%,#1c3565 100%)}
.client-tile{width:165px;height:80px;background:var(--blue);color:var(--white);display:flex;align-items:center;justify-content:center;font-size:22px;font-weight:600}
.clients-title{right:151px;top:1815px;color:var(--white);font-size:38px;font-weight:300}
.clients-title b{font-weight:700}
.clients-sub{right:151px;top:1868px;color:var(--white);font-family:'Open Sans',sans-serif;font-size:12px}

/* contact */
.contact-title{left:154px;top:2045px;font-size:20px;font-weight:700;color:var(--ink)}
.contact-title span{color:var(--blue)}
.contact-rule{left:154px;top:2094px;width:354px;height:1px;background:#bbb}
.contact-copy{left:154px;top:2110px;width:380px;font-family:'Montserrat',sans-serif;font-weight:500;font-size:13.5px;line-height:18px;color:#5a1f1f}
.contact-phone{left:154px;top:2157px;font-size:22px;font-weight:600;color:var(--blue)}
.news-title{left:758px;top:2040px;font-size:20px;font-weight:500;color:var(--ink)}
.news-title span{color:var(--blue)}
.news-sub{left:758px;top:2062px;font-size:11.5px;font-weight:600;color:#3a1c1c}
.news-input{left:758px;top:2096px;width:288px;height:32px;border:1px solid #bdbdbd;font-family:'Open Sans',sans-serif;font-size:10.5px;color:#555;padding-left:12px;display:flex;align-items:center}
.news-btn{left:758px;top:2147px;width:144px;height:33px;background:var(--blue);color:var(--white);font-size:11.5px;font-weight:700;display:flex;align-items:center;justify-content:center}

/* footer */
.footer{left:0;top:2284px;width:1200px;height:317px;background:var(--blue)}
.footer-brand{left:152px;top:2352px;font-size:38px}
.footer-brand .brand-mark{width:40px;height:40px}
.social{left:150px;top:2434px;display:flex;gap:13px}
.social i{width:22px;height:22px;border-radius:50%;border:1.5px solid var(--white)}
.copyright{left:150px;top:2483px;color:var(--white);font-size:9px;letter-spacing:.3px}
.footer-col{color:var(--white);font-family:'Open Sans',sans-serif;font-size:11px;line-height:26px}
.footer-col h4{font-family:'Montserrat',sans-serif;font-size:13px;font-weight:700;letter-spacing:.5px;margin-bottom:12px;line-height:16px}
</style>
</head>
<body>

<header class="abs hero">
  <div class="hero-photo" role="img" aria-label="Photo of a team gathered around a computer in an office"></div>
  <div class="hero-shade"></div>
</header>
<div class="abs brand header-brand"><span class="brand-mark"></span>TovaRoom</div>
<nav class="abs nav">
  <span class="active">HOME</span><span>ABOUT US</span><span>HOW IT WORKS</span><span>SERVICES</span><span>WHY USE US</span><span>FAQ</span>
</nav>
<div class="abs nav-cta">CONTACT US</div>
<h1 class="abs hero-title">Utilising your facility to <b>create</b><br><b>value for your organisation</b><br>and the community.</h1>
<div class="abs hero-btn">GET STARTED</div>
<div class="abs hero-band">We are here to assist. Contact us by phone, email or via our social media channels.</div>

<section>
  <p class="abs eyebrow process-eyebrow">HOW DOES IT THE</p>
  <h2 class="abs section-title process-title">BOOKINGS PROCESS WORK?</h2>
  <p class="abs process-sub">We manage your space and generate more income from your school facilities.</p>

  <div class="abs step step-1" style="left:284px;top:884px">
    <div class="step-shape"></div>
    <svg class="step-icon" viewBox="0 0 60 60" fill="none" stroke="#fff" stroke-width="2"><circle cx="30" cy="22" r="14"/><path d="M16 22h28M30 8c-6 8-6 20 0 28M30 8c6 8 6 20 0 28"/><circle cx="20" cy="46" r="7"/><circle cx="40" cy="46" r="7"/><path d="M27 46h6"/></svg>
    <p class="step-text">Client/hirer looks for advertised space / facility via TovaRoom online platform and makes application</p>
    <div class="step-num">1</div>
  </div>
  <div class="abs step step-2" style="left:496px;top:884px">
    <div class="step-shape"></div>
    <svg class="step-icon" viewBox="0 0 60 60" fill="none" stroke="#fff" stroke-width="2"><rect x="12" y="12" width="36" height="26" rx="2"/><path d="M6 44h48l-4 6H10z"/><circle cx="36" cy="24" r="6"/><path d="M33 24l2 2 4-4M18 20h10M18 26h8M18 32h12"/></svg>
    <p class="step-text">Application evaluated by TovaRoom based on guidelines &amp; criteria agreed with facility (history, insurances)</p>
    <div class="step-num">2</div>
  </div>
  <div class="abs step step-3" style="left:706px;top:884px">
    <div class="step-shape"></div>
    <svg class="step-icon" viewBox="0 0 60 60" fill="none" stroke="#fff" stroke-width="2"><rect x="10" y="12" width="40" height="36" rx="3"/><path d="M10 22h40M20 8v8M40 8v8"/><path d="M16 28h4M24 28h4M32 28h4M16 35h4M24 35h4M16 42h4"/><circle cx="40" cy="40" r="7"/><path d="M37 40l2 2 4-4"/></svg>
    <p class="step-text">Booking of facility made via TovaRoom online bookings platform</p>
    <div class="step-num">3</div>
  </div>
  <div class="abs step step-4" style="left:914px;top:884px">
    <div class="step-shape"></div>
    <svg class="step-icon" viewBox="0 0 60 60" fill="none" stroke="#fff" stroke-width="2"><path d="M16 8h24l6 6v38H16z"/><path d="M22 18h16M22 24h16M22 30h10"/><circle cx="36" cy="40" r="7"/><path d="M33 40l2 2 4-4"/></svg>
    <p class="step-text">Invoice generated and payment received prior to hire of facility</p>
    <div class="step-num">4</div>
  </div>
</section>

<section>
  <div class="abs services"></div>
  <h2 class="abs section-title services-title">SERVICES PROVIDED</h2>
  <p class="abs eyebrow services-eyebrow">BY TOVAROOM</p>

  <div class="abs card" style="left:151px;top:1257px;width:212px;height:318px">
    <div class="card-art" role="img" aria-label="Illustration of a laptop with social media marks" style="top:50px;background:linear-gradient(135deg,#7ec6e8,#3e8fcf)"></div>
    <p class="card-name" style="top:186px">MARKETING &amp; PROMOTION<br>OF YOUR FACILITY</p>
    <div class="card-btn" style="top:246px">Book Now</div>
  </div>
  <div class="abs card" style="left:607px;top:1257px;width:215px;height:318px">
    <div class="card-art" role="img" aria-label="Illustration of a light bulb with a target and arrow" style="top:50px;background:linear-gradient(135deg,#f9d27a,#6cb5e0)"></div>
    <p class="card-name" style="top:186px">ADMINISTER BOOKINGS<br>AND ENQUIRIES</p>
    <div class="card-btn" style="top:246px">Book Now</div>
  </div>
  <div class="abs card" style="left:831px;top:1257px;width:218px;height:318px">
    <div class="card-art" role="img" aria-label="Illustration of a hand holding an invoice" style="top:50px;background:linear-gradient(135deg,#f07b6b,#f6c768)"></div>
    <p class="card-name" style="top:186px">INVOICES &amp; PAYMENT<br>COLLECTION</p>
    <div class="card-btn" style="top:246px">Book Now</div>
  </div>
  <div class="abs card featured" style="left:368px;top:1243px;width:236px;height:345px">
    <div class="card-art" role="img" aria-label="Illustration of two people with speech bubbles" style="top:44px;background:linear-gradient(135deg,#6cc2e6,#f07463)"></div>
    <p class="card-name" style="top:172px">ADMINISTER BOOKINGS<br>AND ENQUIRIES</p>
    <p class="card-copy" style="top:212px">Neque porro quisquam est qui dolorem quia dolor sit amet, consectetur</p>
    <div class="card-btn" style="top:261px">Read More</div>
  </div>
  <div class="abs dots"><i></i><i></i><i></i></div>
</section>

<section>
  <div class="abs clients" role="img" aria-label="Dark blue tinted photo of business people"></div>
  <div class="abs client-tile" style="left:151px;top:1757px">Larkfold</div>
  <div class="abs client-tile" style="left:328px;top:1757px">Brenvia</div>
  <div class="abs client-tile" style="left:505px;top:1757px">Stoneby</div>
  <div class="abs client-tile" style="left:151px;top:1850px">Quillon</div>
  <div class="abs client-tile" style="left:328px;top:1850px">Mareth</div>
  <div class="abs client-tile" style="left:505px;top:1850px">Ostrell &amp; Co</div>
  <h2 class="abs clients-title">OUR <b>CLIENTS</b></h2>
  <p class="abs clients-sub">Some of great beers our great clients</p>
</section>

<section>
  <h3 class="abs contact-title">NEED MORE DETAILS? <span>CONTACT US</span></h3>
  <div class="abs contact-rule"></div>
  <p class="abs contact-copy">We are here to assist. Contact us by phone, email or via our social media channels.</p>
  <p class="abs contact-phone">+ 041 555 0187</p>
  <h3 class="abs news-title">OUR <span>NEWSLETTER</span></h3>
  <p class="abs news-sub">Receive the Latest Deals, News and More.</p>
  <div class="abs news-input">Type your email address</div>
  <div class="abs news-btn">SUBSCRIBE</div>
</section>

<footer>
  <div class="abs footer"></div>
  <div class="abs brand footer-brand"><span class="brand-mark"></span>TovaRoom</div>
  <div class="abs social"><i></i><i></i><i></i><i></i></div>
  <p class="abs copyright">© 2017 Tovaroom Pty. Ltd.. All Rights Reserved</p>
  <div class="abs footer-col" style="left:713px;top:2344px">
    <h4>QUICK LINKS</h4>
    Home<br>About<br>Services<br>News &amp; Updates<br>Contact
  </div>
  <div class="abs footer-col" style="left:898px;top:2344px">
    <h4>CONTACT INFO</h4>
    PO Box 4417<br>Ferndale East VIC 3190<br>info@tovaroom.com
  </div>
</footer>

</body>
</html>
```